Business cards, stationery and report cover
For market research and marketing company in New Zealand
Simple
Rosalind Thorpe
Level 1
57 Pemberly Road
Milford
Auckland
PO Box 46-582
Auckland 0963
rosalind@lumenvex.co.nz
www.lumenvex.co.nz
From this process we are looking for business cards, letterhead, comp slip, as well as a generic cover page and inside page for our reports (e.g heading styles, footers etc). Both report pages need to be easily replicated or applied to Microsoft Word reports. We are PC users if this makes a difference.
The information for the business cards can be on the front or the back - depending on your design and what looks best. Most people would contact us by phone/cell/email.
We would like to be viewed as professional, competent, modern and well established. We don't want to look like we are an advertising agency, or quirky or too different from our competitors. However, we'd like to be eye catching and interesting! Our typical clients are intelligent managers who are over 35 years and a mixture of male and female.
Please let us know if you have any questions or would like clarification on anything.
As noted in 'Additional Comments' you can choose what details would look best on the front of the business card, and which you would recommend going on the back of the card.
This is our new logo.

```html
<!DOCTYPE html>
<html lang="en">
<head>
<meta charset="utf-8">
<title>Lumenvex stationery set</title>
<link href="https://fonts.googleapis.com/css2?family=Open+Sans:wght@400;600&display=swap" rel="stylesheet">
<style>
  :root {
    --brand-blue: #1f7fc1;
    --brand-blue-dark: #176aa3;
    --charcoal: #55585c;
    --ink: #3c3f43;
    --muted: #8a8d91;
    --paper: #ffffff;
    --lining: #7d8085;
    --stage: #e6e6e6;
    --edge: #d2d2d2;
  }
  * { box-sizing: border-box; margin: 0; padding: 0; }
  html, body { width: 1200px; height: 490px; overflow: hidden; }
  body {
    background: var(--stage);
    font-family: "Open Sans", Arial, sans-serif;
    color: var(--ink);
    position: relative;
  }
  .sheet {
    position: absolute;
    background: var(--paper);
    border: 1px solid var(--edge);
  }
  .wordmark {
    font-family: "Open Sans", Arial, sans-serif;
    font-weight: 600;
    color: var(--brand-blue);
    letter-spacing: -0.02em;
    display: flex;
    align-items: center;
    gap: 0.3em;
    line-height: 1;
  }
  .wordmark .dot {
    width: 0.45em; height: 0.45em; border-radius: 50%;
    background: currentColor; display: inline-block;
  }
  .wordmark.on-dark { color: var(--paper); }

  /* Business cards */
  .card { width: 110px; height: 70px; }
  .card .wordmark { font-size: 15px; position: absolute; left: 12px; top: 26px; }
  .card--front { left: 10px; top: 40px; }
  .card--back { left: 126px; top: 40px; padding: 8px 9px; }
  .card--dark { left: 10px; top: 118px; background: var(--charcoal); border-color: var(--charcoal); }
  .card--blue { left: 126px; top: 118px; background: var(--brand-blue); border-color: var(--brand-blue); }
  .card--back .person { font-size: 6.5px; font-weight: 600; color: var(--brand-blue); text-align: right; }
  .card--back .contact { font-size: 4.3px; line-height: 1.45; color: var(--ink); margin-top: 6px; }
  .card--back .wordmark { font-size: 8px; top: auto; bottom: 7px; left: 9px; }

  /* Envelopes */
  .envelope { width: 228px; height: 96px; }
  .envelope--back { left: 10px; top: 200px; overflow: hidden; }
  .envelope--front { left: 6px; top: 236px; }
  .envelope--front .wordmark { font-size: 12px; position: absolute; left: 98px; top: 24px; }
  .envelope .flap { position: absolute; inset: 0; }

  /* Compliment slips */
  .slip { width: 150px; height: 98px; padding: 10px 12px; }
  .slip--left { left: 76px; top: 350px; }
  .slip--right { left: 236px; top: 350px; }
  .slip .wordmark { font-size: 11px; }
  .slip .greeting { position: absolute; left: 12px; bottom: 14px; font-size: 5.5px; color: var(--muted); }

  /* Letterhead */
  .letterhead { left: 394px; top: 38px; width: 172px; height: 424px; }
  .letterhead .wordmark { font-size: 16px; position: absolute; left: 16px; top: 22px; }
  .letterhead .footer {
    position: absolute; left: 10px; right: 10px; bottom: 12px;
    font-size: 3.6px; color: var(--muted); text-align: center; line-height: 1.5;
  }

  /* Report cover */
  .report-cover { left: 586px; top: 34px; width: 226px; height: 444px; overflow: hidden; }
  .report-cover .wordmark { font-size: 25px; position: absolute; left: 22px; top: 72px; }
  .report-cover .rule { position: absolute; left: 0; right: 0; top: 124px; height: 2px; background: var(--brand-blue); }
  .report-cover .title { position: absolute; right: 18px; top: 232px; text-align: right; }
  .report-cover .title h1 { font-size: 15px; font-weight: 400; color: var(--ink); }
  .report-cover .title p { font-size: 11px; color: var(--ink); margin-top: 2px; }
  .report-cover .photo {
    position: absolute; left: 0; right: 0; bottom: 0; height: 140px;
    background: linear-gradient(160deg, #eef3f8 0%, #c6d6e6 45%, #8aa3bf 100%);
  }

  /* Report inside page */
  .report-page { left: 832px; top: 34px; width: 226px; height: 444px; padding: 22px 14px; }
  .report-page .running-head {
    position: absolute; right: 14px; top: 10px; font-size: 4px; color: var(--muted);
  }
  .report-page .columns { display: flex; gap: 10px; margin-top: 10px; }
  .report-page .main { flex: 1; }
  .report-page h2 {
    font-size: 5.5px; font-weight: 600; color: var(--paper); background: var(--brand-blue);
    padding: 2px 4px; margin-bottom: 4px;
  }
  .report-page .main p { font-size: 4.3px; line-height: 1.55; color: var(--ink); margin-bottom: 12px; }
  .report-page .main h2 + p { margin-bottom: 40px; }
  .report-page .sidebar {
    width: 62px; background: var(--brand-blue); color: var(--paper);
    padding: 6px; align-self: flex-start; margin-top: 70px;
  }
  .report-page .sidebar h3 { font-size: 5px; font-weight: 600; margin-bottom: 3px; }
  .report-page .sidebar p { font-size: 4px; line-height: 1.5; }
  .report-page .page-foot {
    position: absolute; left: 14px; right: 14px; bottom: 10px;
    border-top: 1px solid var(--brand-blue); padding-top: 3px;
    font-size: 3.8px; color: var(--muted); display: flex; justify-content: space-between;
  }
</style>
</head>
<body>

  <!-- Business cards -->
  <div class="sheet card card--front">
    <div class="wordmark"><span class="dot"></span>lumenvex</div>
  </div>
  <div class="sheet card card--back">
    <div class="person">Rosalind Thorpe</div>
    <div class="contact">
      Level 1, 57 Pemberly Road, Milford<br>
      PO Box 46-582, Auckland 0963<br>
      rosalind@lumenvex.co.nz<br>
      www.lumenvex.co.nz
    </div>
    <div class="wordmark"><span class="dot"></span>lumenvex</div>
  </div>
  <div class="sheet card card--dark">
    <div class="wordmark on-dark"><span class="dot"></span>lumenvex</div>
  </div>
  <div class="sheet card card--blue">
    <div class="wordmark on-dark"><span class="dot"></span>lumenvex</div>
  </div>

  <!-- Envelopes -->
  <div class="sheet envelope envelope--back">
    <svg class="flap" viewBox="0 0 228 96" preserveAspectRatio="none" aria-hidden="true">
      <path d="M0 0 L228 0 Q120 40 114 70 Q108 40 0 0 Z" fill="var(--lining)"/>
    </svg>
  </div>
  <div class="sheet envelope envelope--front">
    <svg class="flap" viewBox="0 0 228 96" preserveAspectRatio="none" aria-hidden="true">
      <path d="M0 0 Q60 18 114 60 Q168 18 228 0" fill="none" stroke="var(--edge)" stroke-width="1"/>
    </svg>
    <div class="wordmark"><span class="dot"></span>lumenvex</div>
  </div>

  <!-- Compliment slips -->
  <div class="sheet slip slip--left">
    <div class="wordmark"><span class="dot"></span>lumenvex</div>
  </div>
  <div class="sheet slip slip--right">
    <div class="greeting">With Compliments</div>
  </div>

  <!-- Letterhead -->
  <div class="sheet letterhead">
    <div class="wordmark"><span class="dot"></span>lumenvex</div>
    <div class="footer">
      Level 1, 57 Pemberly Road, Milford · PO Box 46-582, Auckland 0963<br>
      rosalind@lumenvex.co.nz · www.lumenvex.co.nz
    </div>
  </div>

  <!-- Report cover -->
  <div class="sheet report-cover">
    <div class="wordmark"><span class="dot"></span>lumenvex</div>
    <div class="rule"></div>
    <div class="title">
      <h1>Brand Research Results</h1>
      <p>ABC Company</p>
    </div>
    <div class="photo" role="img" aria-label="Photograph of research papers and tablets on a desk"></div>
  </div>

  <!-- Report inside page -->
  <div class="sheet report-page">
    <div class="running-head">Brand Research Results</div>
    <div class="columns">
      <div class="main">
        <h2>Background</h2>
        <p>The study explored how managers perceive local brands across key sectors and what drives their choice.</p>
        <h2>Key findings</h2>
        <p>Respondents valued trust, clear pricing and long standing service above novelty or bold advertising claims.</p>
      </div>
      <aside class="sidebar">
        <h3>Summary</h3>
        <p>Trust and service lead brand preference for most decision makers.</p>
      </aside>
    </div>
    <div class="page-foot"><span>lumenvex</span><span>Page 2</span></div>
  </div>

</body>
</html>
```